Sunny Paths and joy Business card

I have a logo, but will like a business card design. Is for a travel agency in Mexico. We focus in family experiences.

I will liek some thing different and unique, from the traditional business card, something to get remmeber for.

Business card information:

Leandro T. Ocampo
leandro@sunnypathsjoy.example

Alameda 482, 3 piso
Col. Tlalpizco
Mexico, D.F. 07320

office: (55) 5000-0142
mobile: (55) 9000-0187

www.sunnypathsjoy.example
@sunnypjoy
blog: sunnypathsandjoy.blogsite.example
facebook: SunnyPathsAndJoy

```html
<!DOCTYPE html>
<html lang="es">
<head>
<meta charset="utf-8">
<title>Sunny Paths and joy – Business card</title>
<link rel="stylesheet" href="https://fonts.googleapis.com/css2?family=Josefin+Sans:wght@600&family=Varela+Round&display=swap">
<style>
  :root {
    --backdrop: #8a6a4c;
    --sky-top: #cfe6f7;
    --sky-bottom: #ffffff;
    --ink: #1d1d1f;
    --brand-blue: #2a6cc6;
    --card-blue: #3b82d8;
    --card-blue-deep: #2a62b8;
    --scenery-blue: #5b98de;
    --hills-green: #7cbf3a;
    --hills-yellow: #e8d94a;
    --white: #ffffff;
  }
  html, body {
    margin: 0;
    width: 1200px;
    height: 900px;
    overflow: hidden;
    background: var(--backdrop);
    font-family: "Varela Round", "Helvetica Neue", Arial, sans-serif;
  }
  .canvas {
    position: relative;
    width: 1200px;
    height: 900px;
  }
  .card {
    position: absolute;
    top: 290px;
    width: 560px;
    height: 320px;
    overflow: hidden;
    box-shadow: 0 10px 24px rgba(0,0,0,.25);
  }

  /* Brand mark (shared) */
  .brand-mark {
    position: absolute;
    display: flex;
    align-items: center;
    gap: 10px;
  }
  .brand-dot {
    width: 30px;
    height: 30px;
    border-radius: 50%;
    background: var(--brand-blue);
    flex: none;
  }
  .brand-name {
    color: var(--brand-blue);
    font-size: 24px;
    line-height: 26px;
    white-space: nowrap;
  }

  /* Front side */
  .card-front {
    left: 30px;
    background: linear-gradient(180deg, var(--sky-top) 0%, var(--sky-bottom) 70%);
  }
  .address {
    position: absolute;
    left: 36px;
    top: 30px;
    margin: 0;
    font-style: normal;
    color: var(--brand-blue);
    font-size: 14px;
    line-height: 20px;
  }
  .card-front .brand-mark {
    right: 40px;
    top: 62px;
  }
  .person-name {
    position: absolute;
    left: 50px;
    top: 156px;
    margin: 0;
    font-family: "Josefin Sans", "Helvetica Neue", Arial, sans-serif;
    font-weight: 600;
    font-size: 31px;
    line-height: 36px;
    letter-spacing: 0.5px;
    text-transform: uppercase;
    color: var(--ink);
  }
  .person-email {
    position: absolute;
    left: 72px;
    top: 198px;
    margin: 0;
    font-size: 15px;
    line-height: 20px;
    color: var(--ink);
  }
  .landscape {
    position: absolute;
    left: 0;
    bottom: 0;
    width: 560px;
    height: 92px;
    background: linear-gradient(180deg, var(--hills-yellow) 0%, var(--hills-green) 55%, #5fa52c 100%);
  }

  /* Back side */
  .card-back {
    left: 610px;
    background: var(--card-blue);
    color: var(--white);
  }
  .back-scenery {
    position: absolute;
    inset: 0;
    background: linear-gradient(160deg, var(--card-blue) 0%, var(--scenery-blue) 55%, var(--card-blue-deep) 100%);
  }
  .card-back .brand-mark {
    left: 34px;
    top: 34px;
  }
  .card-back .brand-dot { background: var(--white); }
  .card-back .brand-name { color: var(--white); }
  .links {
    position: absolute;
    left: 34px;
    top: 128px;
    margin: 0;
    padding: 0;
    list-style: none;
    font-size: 14px;
    line-height: 26px;
  }
  .links li {
    display: flex;
    align-items: center;
    gap: 10px;
  }
  .link-icon {
    width: 12px;
    height: 12px;
    background: var(--white);
    border-radius: 2px;
    flex: none;
  }
  .phones {
    position: absolute;
    right: 30px;
    bottom: 24px;
    margin: 0;
    font-size: 14px;
    line-height: 22px;
    text-align: right;
  }
</style>
</head>
<body>
<main class="canvas">

  <section class="card card-front" aria-label="Card front">
    <address class="address">
      Alameda 482, 3 piso<br>
      Col. Tlalpizco<br>
      Mexico, D.F. 07320
    </address>

    <div class="brand-mark">
      <span class="brand-dot"></span>
      <span class="brand-name">Sunny Paths<br>and joy</span>
    </div>

    <h1 class="person-name">Leandro T. Ocampo</h1>
    <p class="person-email">leandro@sunnypathsjoy.example</p>

    <div class="landscape" role="img" aria-label="Illustrated countryside with rolling green and yellow hills, trees, small houses and a winding road"></div>
  </section>

  <section class="card card-back" aria-label="Card back">
    <div class="back-scenery" role="img" aria-label="Faint illustrated blue mountain scenery filling the card background"></div>

    <div class="brand-mark">
      <span class="brand-dot"></span>
      <span class="brand-name">Sunny Paths<br>and joy</span>
    </div>

    <ul class="links">
      <li><span class="link-icon"></span>www.sunnypathsjoy.example</li>
      <li><span class="link-icon"></span>@sunnypjoy</li>
      <li><span class="link-icon"></span>blog: sunnypathsandjoy.blogsite.example</li>
      <li><span class="link-icon"></span>facebook: SunnyPathsAndJoy</li>
    </ul>

    <p class="phones">
      office: (55) 5000-0142<br>
      mobile: (55) 9000-0187
    </p>
  </section>

</main>
</body>
</html>
```